Breezeway Comfort business cards design

Need a business card design for a Heating and Air Conditioning business. I need these items included.
Business name: Breezeway Comfort
Owner: Marcus Tollefsen
License # 2874590
Phone number # 555-382-4071
Email: breezewaycomfortair@mailvista.example
Sales
Service
Installation
Maintenance

Heating and Air Conditioning

Requirements
Must have
• Company name , license number , phone number , email

```html
<!DOCTYPE html>
<html lang="en">
<head>
<meta charset="utf-8">
<title>Breezeway Comfort – Business Cards</title>
<link href="https://fonts.googleapis.com/css2?family=Exo+2:wght@600&family=Montserrat:wght@400;700&display=swap" rel="stylesheet">
<style>
  :root{
    --bg:#e9eaec;
    --royal:#1c44a0;
    --flame:#ef6340;
    --ink:#1b1b1b;
    --white:#ffffff;
  }
  *{margin:0;padding:0;box-sizing:border-box}
  html,body{width:1200px;height:1200px;overflow:hidden;background:var(--bg)}
  .card{
    position:absolute;left:150px;width:900px;height:514px;border-radius:36px;overflow:hidden;
    box-shadow:0 10px 30px rgba(0,0,0,.18);
  }
  .card--front{top:48px;background:var(--royal)}
  .card--back{top:638px;background:var(--white)}

  .brand{display:flex;align-items:center;gap:18px}
  .brand__dot{width:62px;height:62px;border-radius:50%;background:var(--flame);flex:none}
  .brand__name{font-family:"Exo 2",sans-serif;font-weight:600;text-transform:uppercase;letter-spacing:2px;line-height:1}

  .card--front .brand{position:absolute;left:0;right:0;top:170px;justify-content:center}
  .card--front .brand__dot{width:90px;height:90px}
  .card--front .brand__name{color:var(--white);font-size:62px}
  .services{
    position:absolute;left:0;right:0;top:330px;text-align:center;
    font-family:Montserrat,sans-serif;font-weight:700;font-size:30px;color:var(--white);
  }
  .services .sep{color:var(--flame);margin:0 10px}

  .card--back .brand{position:absolute;left:60px;top:250px;gap:12px}
  .card--back .brand__dot{width:44px;height:44px}
  .card--back .brand__name{color:var(--royal);font-size:30px;max-width:230px}
  .divider{position:absolute;left:345px;top:70px;width:2px;height:210px;background:var(--royal)}
  .contact{position:absolute;left:368px;top:62px;font-family:Montserrat,sans-serif;color:var(--ink)}
  .contact__name{font-family:"Exo 2",sans-serif;font-weight:600;color:var(--royal);font-size:36px;line-height:1.1}
  .contact__role{font-size:19px;margin:4px 0 10px 10px}
  .contact__line{font-size:18px;line-height:30px;display:flex;align-items:center;gap:10px;margin-left:10px}
  .contact__line svg{width:18px;height:18px;flex:none}
  .contact__line--plain{padding-left:0}
  .wave{position:absolute;left:0;bottom:0;width:900px;height:514px}
</style>
</head>
<body>
  <section class="card card--front">
    <div class="brand">
      <span class="brand__dot"></span>
      <span class="brand__name">Breezeway Comfort</span>
    </div>
    <p class="services">Sales<span class="sep">•</span>Service<span class="sep">•</span>Installation<span class="sep">•</span>Maintenance</p>
  </section>

  <section class="card card--back">
    <svg class="wave" viewBox="0 0 900 514" preserveAspectRatio="none">
      <path d="M600 290 C760 270 860 200 900 110 L900 150 C850 240 760 280 600 290 Z" fill="var(--flame)"/>
      <path d="M0 430 C180 300 420 300 640 300 C790 300 870 250 900 200 L900 514 L0 514 Z" fill="var(--royal)"/>
      <path d="M230 395 C380 320 560 318 700 305 C800 296 870 265 895 220" fill="none" stroke="var(--white)" stroke-width="4"/>
    </svg>
    <div class="brand">
      <span class="brand__dot"></span>
      <span class="brand__name">Breezeway Comfort</span>
    </div>
    <div class="divider"></div>
    <div class="contact">
      <h1 class="contact__name">Marcus Tollefsen</h1>
      <p class="contact__role">Owner</p>
      <p class="contact__line">License # 2874590</p>
      <p class="contact__line">
        <svg viewBox="0 0 24 24"><path d="M6.6 10.8a15 15 0 0 0 6.6 6.6l2.2-2.2a1 1 0 0 1 1-.25 11.4 11.4 0 0 0 3.6.57 1 1 0 0 1 1 1V20a1 1 0 0 1-1 1A17 17 0 0 1 3 4a1 1 0 0 1 1-1h3.5a1 1 0 0 1 1 1c0 1.25.2 2.45.57 3.6a1 1 0 0 1-.25 1z" fill="var(--flame)"/></svg>
        555-382-4071
      </p>
      <p class="contact__line">
        <svg viewBox="0 0 24 24"><path d="M2 5h20v14H2z" fill="var(--flame)"/><path d="M2 5l10 8 10-8" fill="none" stroke="var(--white)" stroke-width="2"/></svg>
        breezewaycomfortair@mailvista.example
      </p>
      <p class="contact__line">
        <svg viewBox="0 0 24 24"><circle cx="12" cy="12" r="10" fill="var(--flame)"/><path d="M2 12h20M12 2c3 3 3 17 0 20M12 2c-3 3-3 17 0 20" fill="none" stroke="var(--white)" stroke-width="1.5"/></svg>
        www.breezewaycomfortair.example
      </p>
    </div>
  </section>
</body>
</html>
```